Velliora Events Business Card

We need a business cards that stands out to our clients. We are company who targets prestige clients to spend money with us on experiences, so our image needs to be prestige
Target Market(s)
Corporate
Contact Information for Business Card
There will be four different names on the business cards
Danielle Brontoss
Director
O: 02 5174 2038
M: 0491 652 083
E: info@vellioraevents.example.com.au
Facebook: @vellioraevents
Instagram: vellioraevents
www.vellioraevents.example.com.au
Nathaniel Brontoss
Director
O: 02 5174 2038
M: 0478 205 946
Facebook: @vellioraevents
Instagram: vellioraevents
www.vellioraevents.example.com.au
Elias Dorvek
Director
O: 02 5174 2038
M: 0467 319 752
Facebook: @vellioraevents
Instagram: vellioraevents
www.vellioraevents.example.com.au
Marta Quell
Director
O: 02 5174 2038
Facebook: @vellioraevents
Instagram: vellioraevents
www.vellioraevents.example.com.au
Colors
Designer to choose colors to be used in the design.
Look and feel

```html
<!DOCTYPE html>
<html lang="en">
<head>
<meta charset="utf-8">
<title>Velliora Events – Business Cards</title>
<link href="https://fonts.googleapis.com/css2?family=EB+Garamond:wght@400;500&display=swap" rel="stylesheet">
<style>
  :root {
    --page: #ffffff;
    --navy: #27224f;
    --gold: #d2ae5a;
    --gold-soft: #c9a24e;
    --ink: #f4f2f8;
    --rule: #8a7444;
  }
  html, body {
    margin: 0;
    padding: 0;
    width: 979px;
    height: 1200px;
    overflow: hidden;
    background: var(--page);
  }
  .sheet {
    position: relative;
    width: 979px;
    height: 1200px;
    font-family: "EB Garamond", Georgia, serif;
  }
  .card {
    position: absolute;
    width: 406px;
    height: 244px;
    background: var(--navy);
    overflow: hidden;
  }
  .col-front { left: 72px; }
  .col-back { left: 501px; }
  .row-1 { top: 82px; }
  .row-2 { top: 346px; }
  .row-3 { top: 610px; }
  .row-4 { top: 875px; }

  .wordmark {
    position: absolute;
    color: var(--gold);
    font-weight: 500;
    text-align: center;
    text-transform: uppercase;
    line-height: 1;
  }
  .wordmark .name-main { display: block; }
  .wordmark .name-sub { display: block; }

  .front .wordmark {
    left: 8px;
    width: 160px;
    top: 104px;
  }
  .front .wordmark .name-main { font-size: 17px; letter-spacing: 4px; }
  .front .wordmark .name-sub { font-size: 9px; letter-spacing: 4px; margin-top: 5px; }

  .back .wordmark {
    left: 0;
    width: 406px;
    top: 98px;
  }
  .back .wordmark .name-main { font-size: 24px; letter-spacing: 7px; }
  .back .wordmark .name-sub { font-size: 12px; letter-spacing: 6px; margin-top: 8px; }

  .divider {
    position: absolute;
    left: 166px;
    top: 43px;
    width: 1px;
    height: 158px;
    background: var(--rule);
  }
  .details {
    position: absolute;
    left: 182px;
    top: 48px;
    color: var(--ink);
  }
  .person-name {
    margin: 0;
    font-size: 17.5px;
    font-weight: 500;
    line-height: 1;
  }
  .person-role {
    margin: 3px 0 10px;
    font-size: 11px;
    color: var(--gold-soft);
    line-height: 1;
  }
  .contact-list {
    list-style: none;
    margin: 0;
    padding: 0;
  }
  .contact-list li {
    display: flex;
    align-items: center;
    height: 17.2px;
    font-size: 11.5px;
    white-space: nowrap;
  }
  .contact-list svg {
    width: 9px;
    height: 9px;
    margin-right: 7px;
    flex: none;
  }
  .icon-stroke { fill: none; stroke: var(--gold); stroke-width: 1.3; }
  .icon-fill { fill: var(--gold); }
</style>
</head>
<body>
<main class="sheet">

  <svg width="0" height="0" style="position:absolute" aria-hidden="true">
    <defs>
      <symbol id="icon-phone" viewBox="0 0 10 10"><path class="icon-fill" d="M2 0.5 L3.6 2.6 L2.7 3.6 C3.3 5 4.9 6.6 6.4 7.3 L7.4 6.4 L9.5 8 L8.4 9.5 C4.5 9.2 0.8 5.5 0.5 1.6 Z"/></symbol>
      <symbol id="icon-mobile" viewBox="0 0 10 10"><rect class="icon-stroke" x="2.6" y="0.7" width="4.8" height="8.6" rx="0.8"/><line class="icon-stroke" x1="4.3" y1="8" x2="5.7" y2="8"/></symbol>
      <symbol id="icon-mail" viewBox="0 0 10 10"><rect class="icon-stroke" x="0.7" y="2" width="8.6" height="6" rx="0.5"/><path class="icon-stroke" d="M0.9 2.3 L5 5.4 L9.1 2.3"/></symbol>
      <symbol id="icon-dot" viewBox="0 0 10 10"><circle class="icon-stroke" cx="5" cy="5" r="3.6"/></symbol>
      <symbol id="icon-square" viewBox="0 0 10 10"><rect class="icon-stroke" x="1.3" y="1.3" width="7.4" height="7.4" rx="1.6"/></symbol>
      <symbol id="icon-globe" viewBox="0 0 10 10"><circle class="icon-stroke" cx="5" cy="5" r="4.2"/><ellipse class="icon-stroke" cx="5" cy="5" rx="1.8" ry="4.2"/><line class="icon-stroke" x1="0.8" y1="5" x2="9.2" y2="5"/></symbol>
    </defs>
  </svg>

  <!-- Row 1 -->
  <section class="card front col-front row-1">
    <div class="wordmark"><span class="name-main">Velliora</span><span class="name-sub">Events</span></div>
    <div class="divider"></div>
    <div class="details">
      <h2 class="person-name">Danielle Brontoss</h2>
      <p class="person-role">Director</p>
      <ul class="contact-list">
        <li><svg><use href="#icon-phone"/></svg>02 5174 2038</li>
        <li><svg><use href="#icon-mobile"/></svg>0491 652 083</li>
        <li><svg><use href="#icon-mail"/></svg>info@vellioraevents.example.com.au</li>
        <li><svg><use href="#icon-dot"/></svg>@vellioraevents</li>
        <li><svg><use href="#icon-square"/></svg>vellioraevents</li>
        <li><svg><use href="#icon-globe"/></svg>www.vellioraevents.example.com.au</li>
      </ul>
    </div>
  </section>
  <section class="card back col-back row-1">
    <div class="wordmark"><span class="name-main">Velliora</span><span class="name-sub">Events</span></div>
  </section>

  <!-- Row 2 -->
  <section class="card front col-front row-2">
    <div class="wordmark"><span class="name-main">Velliora</span><span class="name-sub">Events</span></div>
    <div class="divider"></div>
    <div class="details">
      <h2 class="person-name">Nathaniel Brontoss</h2>
      <p class="person-role">Director</p>
      <ul class="contact-list">
        <li><svg><use href="#icon-phone"/></svg>02 5174 2038</li>
        <li><svg><use href="#icon-mobile"/></svg>0478 205 946</li>
        <li><svg><use href="#icon-mail"/></svg>info@vellioraevents.example.com.au</li>
        <li><svg><use href="#icon-dot"/></svg>@vellioraevents</li>
        <li><svg><use href="#icon-square"/></svg>vellioraevents</li>
        <li><svg><use href="#icon-globe"/></svg>www.vellioraevents.example.com.au</li>
      </ul>
    </div>
  </section>
  <section class="card back col-back row-2">
    <div class="wordmark"><span class="name-main">Velliora</span><span class="name-sub">Events</span></div>
  </section>

  <!-- Row 3 -->
  <section class="card front col-front row-3">
    <div class="wordmark"><span class="name-main">Velliora</span><span class="name-sub">Events</span></div>
    <div class="divider"></div>
    <div class="details">
      <h2 class="person-name">Elias Dorvek</h2>
      <p class="person-role">Director</p>
      <ul class="contact-list">
        <li><svg><use href="#icon-phone"/></svg>02 5174 2038</li>
        <li><svg><use href="#icon-mobile"/></svg>0467 319 752</li>
        <li><svg><use href="#icon-mail"/></svg>info@vellioraevents.example.com.au</li>
        <li><svg><use href="#icon-dot"/></svg>@vellioraevents</li>
        <li><svg><use href="#icon-square"/></svg>vellioraevents</li>
        <li><svg><use href="#icon-globe"/></svg>www.vellioraevents.example.com.au</li>
      </ul>
    </div>
  </section>
  <section class="card back col-back row-3">
    <div class="wordmark"><span class="name-main">Velliora</span><span class="name-sub">Events</span></div>
  </section>

  <!-- Row 4 -->
  <section class="card front col-front row-4">
    <div class="wordmark"><span class="name-main">Velliora</span><span class="name-sub">Events</span></div>
    <div class="divider"></div>
    <div class="details" style="top:52px">
      <h2 class="person-name">Marta Quell</h2>
      <p class="person-role">Director</p>
      <ul class="contact-list">
        <li><svg><use href="#icon-phone"/></svg>02 5174 2038</li>
        <li><svg><use href="#icon-mail"/></svg>info@vellioraevents.example.com.au</li>
        <li><svg><use href="#icon-dot"/></svg>@vellioraevents</li>
        <li><svg><use href="#icon-square"/></svg>vellioraevents</li>
        <li><svg><use href="#icon-globe"/></svg>www.vellioraevents.example.com.au</li>
      </ul>
    </div>
  </section>
  <section class="card back col-back row-4">
    <div class="wordmark"><span class="name-main">Velliora</span><span class="name-sub">Events</span></div>
  </section>

</main>
</body>
</html>
```